PLOVEN Business Card

Coastal Build Additions and Refits. I need a business card designed for this new high end renovation business. I would like the logo centered on the back side with the ABN (37 915 402 176) on the bottom right hand corner.

I would like the following information placed on the other side along with some customized pattern or design.

Derek Collwood
Director
Phone: 1300 480 957
Fax: (02) 8145 9021
Website: www.plovenbuilders.com.au
Email: d.collwood@plovenbuilders.com.au
PO Box 87,
Kelvinbrook NSW 2069

(FB Logo) PLOVEN - Coastal Build Additions and Refits

The final design should communicate professionalism and trust.

Back side background colour: white
Front side: Undecided

```html
<!DOCTYPE html>
<html lang="en">
<head>
<meta charset="utf-8">
<title>PLOVEN Business Card</title>
<link rel="stylesheet" href="https://fonts.googleapis.com/css2?family=Crimson+Text:wght@400;600;700&display=swap">
<style>
  :root {
    --page-bg: #e9e9ea;
    --card-white: #ffffff;
    --brand-blue: #1f6fbd;
    --name-blue: #1c5a9c;
    --ink: #1a1a1a;
    --charcoal: #333335;
    --web-grey: #a9a9ab;
    --shadow: rgba(0, 0, 0, 0.18);
  }
  * { box-sizing: border-box; margin: 0; padding: 0; }
  html, body {
    width: 1200px;
    height: 926px;
    overflow: hidden;
    background: var(--page-bg);
    font-family: "Crimson Text", Georgia, serif;
    color: var(--ink);
  }
  .canvas {
    position: relative;
    width: 1200px;
    height: 926px;
  }
  .card {
    position: absolute;
    left: 280px;
    width: 640px;
    height: 390px;
    background: var(--card-white);
    box-shadow: 0 6px 22px var(--shadow);
    overflow: hidden;
  }
  .card--back { top: 48px; }
  .card--front { top: 488px; }

  /* Wordmark */
  .wordmark {
    position: absolute;
    left: 0;
    right: 0;
    text-align: center;
  }
  .wordmark__name {
    display: block;
    font-weight: 600;
    color: var(--ink);
    letter-spacing: 0.04em;
    line-height: 1;
  }
  .wordmark__tagline {
    display: flex;
    align-items: center;
    justify-content: center;
    gap: 8px;
    color: var(--brand-blue);
    font-weight: 400;
    text-transform: uppercase;
    letter-spacing: 0.03em;
    line-height: 1;
  }
  .wordmark__tagline::before,
  .wordmark__tagline::after {
    content: "";
    height: 1.5px;
    background: var(--brand-blue);
  }

  .card--back .wordmark { top: 92px; }
  .card--back .wordmark__name { font-size: 74px; }
  .card--back .wordmark__tagline { font-size: 18px; margin-top: 4px; }
  .card--back .wordmark__tagline::before,
  .card--back .wordmark__tagline::after { width: 46px; }

  .abn-band {
    position: absolute;
    left: 0;
    right: 0;
    top: 232px;
    height: 82px;
    background: var(--brand-blue);
    color: var(--card-white);
    display: flex;
    align-items: center;
    justify-content: center;
    font-size: 22px;
    letter-spacing: 0.03em;
  }

  /* Front */
  .card--front .wordmark { top: 26px; right: 40px; }
  .card--front .wordmark__name { font-size: 50px; }
  .card--front .wordmark__tagline { font-size: 12.5px; margin-top: 3px; }
  .card--front .wordmark__tagline::before,
  .card--front .wordmark__tagline::after { width: 30px; }

  .person {
    position: absolute;
    top: 112px;
    left: 0;
    right: 30px;
    text-align: center;
    font-size: 27px;
    color: var(--name-blue);
  }
  .person__surname { font-weight: 700; }
  .person__role {
    font-size: 16px;
    color: var(--ink);
    letter-spacing: 0.06em;
    margin-left: 4px;
  }

  .contact {
    position: absolute;
    top: 158px;
    left: 0;
    right: 0;
    text-align: center;
    list-style: none;
    font-size: 16.5px;
    line-height: 1.3;
  }
  .contact__label { font-weight: 700; }

  .front-base {
    position: absolute;
    left: 0;
    bottom: 0;
    width: 640px;
    height: 390px;
  }
  .website {
    position: absolute;
    left: 56px;
    bottom: 22px;
    font-size: 18px;
    letter-spacing: 0.09em;
    color: var(--web-grey);
  }
</style>
</head>
<body>
<main class="canvas">

  <section class="card card--back" aria-label="Card back">
    <div class="wordmark">
      <span class="wordmark__name">PLOVEN</span>
      <span class="wordmark__tagline">Coastal Build Additions &amp; Refits</span>
    </div>
    <div class="abn-band">ABN (37 915 402 176)</div>
  </section>

  <section class="card card--front" aria-label="Card front">
    <svg class="front-base" viewBox="0 0 640 390" aria-hidden="true">
      <path d="M0 302 C150 332 300 354 430 350 C530 346 600 312 640 292 L640 390 L0 390 Z" fill="var(--charcoal)"/>
      <path d="M0 282 C120 290 260 316 410 338 C270 326 130 308 0 298 Z" fill="var(--brand-blue)"/>
    </svg>

    <div class="wordmark">
      <span class="wordmark__name">PLOVEN</span>
      <span class="wordmark__tagline">Coastal Build Additions &amp; Refits</span>
    </div>

    <p class="person">Derek <span class="person__surname">Collwood</span><span class="person__role">-Director</span></p>

    <ul class="contact">
      <li><span class="contact__label">phone:</span> 1300 480 957</li>
      <li><span class="contact__label">fax:</span> (02) 8145 9021</li>
      <li><span class="contact__label">email:</span> d.collwood@plovenbuilders.com.au</li>
      <li><span class="contact__label">addres:</span> PO Box 87, Kelvinbrook NSW 2069</li>
    </ul>

    <p class="website">www.plovenbuilders.com.au</p>
  </section>

</main>
</body>
</html>
```